Flyer-Design für psychologische Beratungspraxis für Mütter
Zielgruppe
Gelassenheitswerkstatt ist eine psychologische Beratungspraxis. Ich unterstütze Mütter, Schwangere und Frauen mit Kinderwunsch bei Herausforderungen rund um Schwangerschaft, Geburt, Mutterschaft, und damit einhergehenden Problemen.
Aufgabenstellung
Text nochmal geringgradig geändert...siehe Datei anbei

```html
<!DOCTYPE html>
<html lang="de">
<head>
<meta charset="utf-8">
<title>Gelassenheitswerkstatt – Flyer</title>
<link rel="stylesheet" href="https://fonts.googleapis.com/css2?family=Gochi+Hand&family=Arimo:wght@400;700&display=swap">
<style>
  :root {
    --bg: #e6e5e2;
    --paper: #f4f4f2;
    --navy: #3b3f8c;
    --pill: #ecebea;
    --photo-top: #c8bdb4;
    --photo-mid: #e2a878;
    --photo-low: #b58867;
    --photo-base: #5f5049;
    --portrait: #cdb9a3;
    --white: #ffffff;
  }
  * { margin: 0; padding: 0; box-sizing: border-box; }
  html, body { width: 1200px; height: 864px; overflow: hidden; }
  body {
    background: var(--bg);
    font-family: "Arimo", Arial, sans-serif;
    display: flex; align-items: center; justify-content: center;
  }
  .flyer {
    width: 1040px; height: 520px;
    display: flex;
    box-shadow: 0 12px 30px rgba(0,0,0,.12);
  }
  .panel { position: relative; width: 520px; height: 520px; overflow: hidden; }

  /* back cover */
  .back-cover { background: var(--paper); color: var(--navy); }
  .portrait {
    position: absolute; left: 28px; top: 70px;
    width: 190px; height: 190px; border-radius: 50%;
    background: radial-gradient(circle at 45% 40%, #e3d3c1, var(--portrait) 60%, #9f8a78);
  }
  .brand {
    position: absolute; left: 270px; top: 78px;
    display: flex; align-items: center; gap: 8px;
    font-weight: 700; font-size: 15px; color: var(--navy);
  }
  .brand-dot { width: 16px; height: 16px; border-radius: 50%; background: var(--navy); }
  .back-heading {
    position: absolute; left: 28px; top: 290px;
    font-weight: 700; font-size: 17px; letter-spacing: .2px;
  }
  .contact {
    position: absolute; left: 40px; top: 322px;
    font-size: 13px; line-height: 1.35;
  }
  .contact .name { font-weight: 700; }
  .contact .gap { margin-top: 14px; }
  .languages {
    position: absolute; right: 40px; bottom: 70px;
    display: flex; gap: 8px;
  }
  .languages svg { width: 26px; height: 16px; display: block; }

  /* front cover */
  .front-cover {
    background: linear-gradient(180deg, var(--photo-top) 0%, #d6b7a0 28%, var(--photo-mid) 48%, var(--photo-low) 70%, var(--photo-base) 100%);
  }
  .front-photo { position: absolute; inset: 0; }
  .title { position: absolute; left: 40px; top: 80px; }
  .title-line {
    display: inline-block;
    background: var(--pill); color: var(--navy);
    font-family: "Gochi Hand", cursive;
    font-size: 28px; letter-spacing: 2px; text-transform: uppercase;
    padding: 2px 18px; border-radius: 22px; margin-bottom: 8px;
  }
  .title-line.second { margin-left: 28px; }
  .subtitle {
    position: absolute; left: 70px; top: 196px;
    color: var(--white); font-size: 13px; line-height: 1.4; opacity: .9;
  }
  .front-brand {
    position: absolute; right: 30px; bottom: 110px;
    color: var(--white); font-size: 11px; font-weight: 700;
  }
</style>
</head>
<body>
  <main class="flyer">
    <section class="panel back-cover">
      <div class="portrait" role="img" aria-label="Porträtfoto der Beraterin am Schreibtisch"></div>
      <div class="brand"><span class="brand-dot"></span>Gelassenheitswerkstatt</div>
      <h2 class="back-heading">KRISENBEGLEITUNG &amp; LEBENSBERATUNG</h2>
      <div class="contact">
        <p class="name">Dr. Carla Benedetti</p>
        <p>Systemische Beraterin (VSBe)</p>
        <p>Heilpraktikerin für Psychotherapie</p>
        <p class="gap">www.gelassenheitswerkstatt.de</p>
        <p>info@gelassenheitswerkstatt.de</p>
        <p class="gap">0151 482 17 305</p>
      </div>
      <div class="languages">
        <svg viewBox="0 0 26 16" aria-label="Deutsch"><rect width="26" height="5.4" fill="#1a1a1a"/><rect y="5.3" width="26" height="5.4" fill="#d22"/><rect y="10.6" width="26" height="5.4" fill="#f5c400"/></svg>
        <svg viewBox="0 0 26 16" aria-label="Italienisch"><rect width="8.7" height="16" fill="#1a8a3c"/><rect x="8.6" width="8.8" height="16" fill="#fff"/><rect x="17.3" width="8.7" height="16" fill="#d22"/></svg>
        <svg viewBox="0 0 26 16" aria-label="Englisch"><rect width="26" height="16" fill="#243a7a"/><path d="M0 0L26 16M26 0L0 16" stroke="#fff" stroke-width="3"/><path d="M0 0L26 16M26 0L0 16" stroke="#c22" stroke-width="1"/><path d="M13 0V16M0 8H26" stroke="#fff" stroke-width="5"/><path d="M13 0V16M0 8H26" stroke="#c22" stroke-width="3"/></svg>
        <svg viewBox="0 0 26 16" aria-label="Französisch"><rect width="8.7" height="16" fill="#2a46a0"/><rect x="8.6" width="8.8" height="16" fill="#fff"/><rect x="17.3" width="8.7" height="16" fill="#d22"/></svg>
      </div>
    </section>

    <section class="panel front-cover">
      <div class="front-photo" role="img" aria-label="Foto: Mutter hält ihr Kind bei Sonnenuntergang am Meer, von hinten gesehen"></div>
      <h1 class="title">
        <span class="title-line">Krisenbegleitung</span><br>
        <span class="title-line second">und Lebensberatung</span>
      </h1>
      <p class="subtitle">Psychologische Beratungspraxis für Mütter,<br>Schwangere und Frauen mit Kinderwunsch</p>
      <div class="front-brand">Gelassenheitswerkstatt</div>
    </section>
  </main>
</body>
</html>
```